Helicopter Tour Brochure Design (8.5 x 11" Bi-Fold Brochure)

Flyer Design for Helicopter Sightseeing Tours. Should be very inviting and touristy. Read "must have" section for more information.

Target Market(s)

Tourists visiting Florida

Industry/Entity Type

Aviation

Colors
3176b5
0456a4
85acd3
757575
9d9d9d
1b1b1b

Requirements
Must have
• Must include the Tour photos and "Route map", so customers know where the tours travels along. It must be inviting.
• Also, design must be for a 8.5 x 11" bi-fold brochure/flyer and include a brief description about our company:
• " Corvane Aviation offers unparalleled sightseeing opportunities with a commitment to safety & customer service. The view during our sightseeing tours will provide for your comfort & more beauty than you ever imagined. And like many of our customers, you’ll want to tell your friends all about it! Corvane Aviation’s experienced pilots will provide a comfortable flight leaving you with a smile on your face. Departure location will be the Pellmont Airport, unless otherwise requested with our office. "
• You can find the tour description online at www.corvanefly.com/tours, which should be included as well.
• Must be in PDF Format.
• 8.5 x 11" Bi-Fold Brochure
• ATTACHED ARE THE DETAILED FORMAT INFORMATION.

```html
<!DOCTYPE html>
<html lang="en">
<head>
<meta charset="utf-8">
<title>Corvane Aviation – Sightseeing Tours Flyer</title>
<link rel="stylesheet" href="https://fonts.googleapis.com/css2?family=Titillium+Web:ital,wght@0,400;0,600;0,700;1,400&family=Open+Sans:wght@400;600&display=swap">
<style>
  :root{
    --blue:#0456a4;
    --sky:#3176b5;
    --cyan:#1ea0dc;
    --head:#1e8fd0;
    --pale:#85acd3;
    --grey:#757575;
    --grey-light:#9d9d9d;
    --ink:#1b1b1b;
    --paper:#ffffff;
    --mist:#f1f3f6;
    --backdrop:#e4e6e9;
  }
  *{box-sizing:border-box;margin:0;padding:0}
  html,body{width:1200px;height:767px;overflow:hidden;background:var(--backdrop)}
  body{position:relative;font-family:"Titillium Web",sans-serif}
  .page{position:absolute;top:73px;width:497px;height:643px;overflow:hidden;
    background:linear-gradient(160deg,var(--cyan) 0%,var(--sky) 45%,var(--blue) 100%);
    box-shadow:0 6px 18px rgba(0,0,0,.25)}
  .page--front{left:77px}
  .page--back{left:632px}
  .shapes{position:absolute;inset:0}
  .brand{position:absolute;color:var(--blue);font-weight:700;line-height:1;text-align:center}
  .brand__name{display:block;font-size:40px;letter-spacing:1px}
  .brand__sub{display:block;font-size:10px;letter-spacing:9px;margin-top:2px}
  .title{position:absolute;color:var(--paper);font-weight:700;font-size:36px;line-height:39px;letter-spacing:.5px}
  .subtitle{position:absolute;color:var(--paper);font-style:italic;font-size:11.5px;line-height:15.5px}
  .copy{position:absolute;color:var(--paper);font-size:9.8px;line-height:12.2px;text-align:justify}
  .copy p+p{margin-top:12px}
  .cert{position:absolute;color:var(--paper);font-style:italic;font-size:7px;line-height:12px;left:22px;top:522px;width:95px}
  .tour-list{position:absolute;left:271px;top:326px;list-style:none}
  .tour-list__head{color:var(--head);font-weight:700;font-size:12.5px;margin-bottom:4px}
  .tour-list li{display:flex;align-items:center;gap:6px;color:var(--ink);font-size:10.5px;height:18.7px}
  .tour-list svg{width:9px;height:9px}
  .thumb{position:absolute;top:484px;width:118px;height:102px;border-radius:6px;transform:skewX(-7deg);box-shadow:0 2px 5px rgba(0,0,0,.3)}
  .footer{position:absolute;left:0;right:0;bottom:0;height:44px;
    background:linear-gradient(90deg,var(--ink) 0%,#222 45%,#3a3a3a 46%,#2c2c2c 100%);
    display:flex;align-items:center;justify-content:space-between;padding:0 20px 0 22px;
    font-family:"Open Sans",sans-serif;color:var(--paper)}
  .footer__url{font-size:15px;letter-spacing:.5px}
  .footer__phone{display:flex;align-items:center;gap:9px;font-size:19px;font-weight:600;letter-spacing:.5px}
  .footer__phone svg{width:20px;height:20px}
  .map{position:absolute;top:242px;width:92px;height:81px;border-radius:6px;transform:skewX(-7deg);
    background:linear-gradient(135deg,#f4f1e6,#dfe6ee);box-shadow:0 2px 5px rgba(0,0,0,.3)}
  .tour{position:absolute}
  .tour__head{display:flex;align-items:center;gap:7px;font-weight:700;font-size:12.5px;height:22px}
  .tour__head svg{width:26px;height:22px}
  .tour__text{font-size:7.6px;line-height:9.7px;text-align:justify;margin-top:4px}
  .tour--light .tour__head,.tour--light .tour__text{color:var(--paper)}
  .tour--dark .tour__head{color:var(--blue)}
  .tour--dark .tour__text{color:var(--grey)}
</style>
</head>
<body>

<section class="page page--front">
  <svg class="shapes" viewBox="0 0 497 643" aria-hidden="true">
    <path d="M19 0 H497 V29 L66 122 Q30 130 27 100 Z" fill="#fff"/>
    <path d="M252 302 L497 270 V643 H190 Z" fill="#fff"/>
  </svg>
  <svg class="shapes" viewBox="0 0 497 643" role="img" aria-label="Photo of a helmeted pilot in an open helicopter door above green Florida countryside">
    <defs><linearGradient id="pilotPhoto" x1="0" y1="0" x2="1" y2="1">
      <stop offset="0" stop-color="#8fb4c8"/><stop offset=".5" stop-color="#3d5f3a"/><stop offset="1" stop-color="#1d3566"/></linearGradient></defs>
    <path d="M292 49 L497 14 V284 L470 320 Q462 328 450 326 L252 302 Z" fill="url(#pilotPhoto)"/>
  </svg>

  <div class="brand" style="left:35px;top:20px"><span class="brand__name">CORVANE</span><span class="brand__sub">AVIATION</span></div>

  <h1 class="title" style="left:22px;top:142px">SIGHTSEEING<br>TOURS</h1>
  <p class="subtitle" style="left:22px;top:227px">Corvane Aviation – Your Aerial Solutions Specialist</p>

  <div class="copy" style="left:22px;top:322px;width:196px">
    <p>Corvane Aviation offers unparalleled sightseeing opportunities with a commitment to safety &amp; customer service. The view during our sightseeing tours will provide for your comfort &amp; more beauty than you ever imagined.</p>
    <p>And like many of our customers, you’ll want to tell your friends all about it! Corvane Aviation’s experienced pilots will provide a comfortable flight leaving you with a smile on your face. Departure will be the Pellmont Airport, unless otherwise requested with our office.</p>
  </div>

  <p class="cert">OAS Carded Equipment and Pilots 14 CFR Part 133, 135, 137 and 91.147 Certified</p>

  <ul class="tour-list">
    <li class="tour-list__head">SIGHTSEEING TOURS</li>
    <li><svg viewBox="0 0 10 10"><circle cx="5" cy="5" r="4.3" fill="none" stroke="#1e8fd0"/><path d="M3 5.2 4.5 6.6 7.2 3.6" fill="none" stroke="#1e8fd0" stroke-width="1.2"/></svg>The QUICKIE</li>
    <li><svg viewBox="0 0 10 10"><circle cx="5" cy="5" r="4.3" fill="none" stroke="#1e8fd0"/><path d="M3 5.2 4.5 6.6 7.2 3.6" fill="none" stroke="#1e8fd0" stroke-width="1.2"/></svg>The DOWNTOWN Tour</li>
    <li><svg viewBox="0 0 10 10"><circle cx="5" cy="5" r="4.3" fill="none" stroke="#1e8fd0"/><path d="M3 5.2 4.5 6.6 7.2 3.6" fill="none" stroke="#1e8fd0" stroke-width="1.2"/></svg>The DELUXE Tour</li>
    <li><svg viewBox="0 0 10 10"><circle cx="5" cy="5" r="4.3" fill="none" stroke="#1e8fd0"/><path d="M3 5.2 4.5 6.6 7.2 3.6" fill="none" stroke="#1e8fd0" stroke-width="1.2"/></svg>The ROMANTIC Tour</li>
    <li><svg viewBox="0 0 10 10"><circle cx="5" cy="5" r="4.3" fill="none" stroke="#1e8fd0"/><path d="M3 5.2 4.5 6.6 7.2 3.6" fill="none" stroke="#1e8fd0" stroke-width="1.2"/></svg>The ULTIMATE BEACH Tour</li>
    <li><svg viewBox="0 0 10 10"><circle cx="5" cy="5" r="4.3" fill="none" stroke="#1e8fd0"/><path d="M3 5.2 4.5 6.6 7.2 3.6" fill="none" stroke="#1e8fd0" stroke-width="1.2"/></svg>The SUNSET Tour</li>
    <li><svg viewBox="0 0 10 10"><circle cx="5" cy="5" r="4.3" fill="none" stroke="#1e8fd0"/><path d="M3 5.2 4.5 6.6 7.2 3.6" fill="none" stroke="#1e8fd0" stroke-width="1.2"/></svg>Introductory FLYING Lesson</li>
  </ul>

  <div class="thumb" style="left:124px;background:linear-gradient(160deg,#a9cbe6,#4c7fa8 60%,#6e7c86)" role="img" aria-label="Aerial photo of a causeway bridge over the bay"></div>
  <div class="thumb" style="left:249px;background:linear-gradient(160deg,#7fb3e0,#d9c9a6 55%,#3f6b4a)" role="img" aria-label="Aerial photo of a waterfront condominium tower"></div>
  <div class="thumb" style="left:374px;background:linear-gradient(160deg,#9cc6ea,#c8d0d6 45%,#2e6f9c)" role="img" aria-label="Aerial photo of a downtown marina and skyline"></div>

  <footer class="footer">
    <span class="footer__url">www.corvanefly.com</span>
    <span class="footer__phone"><svg viewBox="0 0 20 20"><circle cx="10" cy="10" r="9" fill="none" stroke="#fff" stroke-width="1.5"/><path d="M7 5.5 8.6 7.8 7.6 9a6 6 0 0 0 3.4 3.4l1.2-1 2.3 1.6-.9 1.6c-3.8.2-7.5-3.5-7.3-7.3Z" fill="#fff"/></svg>+1 (555) 014-2290</span>
  </footer>
</section>

<section class="page page--back">
  <svg class="shapes" viewBox="0 0 497 643" aria-hidden="true">
    <path d="M0 0 H497 V70 L480 74 Q476 126 448 122 L0 28 Z" fill="#fff"/>
    <path d="M248 325 L497 264 V643 H196 Z" fill="var(--mist)"/>
  </svg>
  <svg class="shapes" viewBox="0 0 497 643" role="img" aria-label="Photo of the city waterfront skyline lit up at dusk">
    <defs><linearGradient id="duskPhoto" x1="0" y1="0" x2="0" y2="1">
      <stop offset="0" stop-color="#3b5a96"/><stop offset=".45" stop-color="#7a6f95"/><stop offset=".7" stop-color="#1d2b4a"/><stop offset="1" stop-color="#2a3c56"/></linearGradient></defs>
    <path d="M285 97 L497 60 V264 L260 322 Z" fill="url(#duskPhoto)"/>
  </svg>

  <div class="brand" style="left:293px;top:20px"><span class="brand__name">CORVANE</span><span class="brand__sub">AVIATION</span></div>

  <h1 class="title" style="left:24px;top:100px">SIGHTSEEING<br>TOURS</h1>
  <p class="subtitle" style="left:24px;top:184px;width:222px">Visit us for an unforgettable experience viewing scenic Florida beaches, Downtown Sarasota and its attractions.</p>

  <div class="map" style="left:24px" role="img" aria-label="Route map of the Quickie and Downtown tours"></div>
  <div class="map" style="left:122px" role="img" aria-label="Route map of the Deluxe and Romantic tours"></div>
  <div class="map" style="left:218px" role="img" aria-label="Route map of the Ultimate Beach and Sunset tours"></div>

  <article class="tour tour--light" style="left:18px;top:341px;width:206px">
    <h2 class="tour__head"><svg viewBox="0 0 26 22"><g fill="none" stroke="#fff" stroke-width="1.6"><path d="M3 3h20M13 3v4"/><circle cx="13" cy="12" r="5"/><path d="M7 20h12M10 17v3M16 17v3"/></g></svg>The QUICKIE</h2>
    <p class="tour__text">(Approx. 10-Minute flight time) Ready for a quick thrill? This is your chance! Take a ride to Downtown, over Sarasota Bay, Bird Key and back! Experience Florida and Sarasota’s Skyline from your own magic carpet.</p>
  </article>
  <article class="tour tour--light" style="left:18px;top:428px;width:192px">
    <h2 class="tour__head"><svg viewBox="0 0 26 22"><g fill="none" stroke="#fff" stroke-width="1.6"><path d="M3 3h20M13 3v4"/><circle cx="13" cy="12" r="5"/><path d="M7 20h12M10 17v3M16 17v3"/></g></svg>The DOWNTOWN Tour</h2>
    <p class="tour__text">(Approx. 20-Minute flight time) Experience the beauty of Downtown Sarasota including an up-close view of the Bayview Art Museum, Marlowe Performing Arts Hall, the Harborline Hotel, Causeway Bridge and Bird Key.</p>
  </article>
  <article class="tour tour--light" style="left:18px;top:516px;width:176px">
    <h2 class="tour__head"><svg viewBox="0 0 26 22"><g fill="none" stroke="#fff" stroke-width="1.6"><path d="M3 3h20M13 3v4"/><circle cx="13" cy="12" r="5"/><path d="M7 20h12M10 17v3M16 17v3"/></g></svg>The DELUXE Tour</h2>
    <p class="tour__text">(Approx. 1-Hour flight time) This special VIP Tour combines all the sights of our DOWNTOWN and ULTIMATE BEACH Tours and is our most exciting and exhilarating sightseeing option with many great locations and landmarks.</p>
  </article>

  <article class="tour tour--dark" style="left:259px;top:341px;width:222px">
    <h2 class="tour__head"><svg viewBox="0 0 26 22"><g fill="none" stroke="#0456a4" stroke-width="1.6"><path d="M3 3h20M13 3v4"/><circle cx="13" cy="12" r="5"/><path d="M7 20h12M10 17v3M16 17v3"/></g></svg>The ROMANTIC Tour</h2>
    <p class="tour__text">(Approx. 20-Minute flight time) Our NEWEST helicopter tour includes romantic music and complimentary Champagne during your flight. Each tour is guaranteed to be private while experiencing the beauty of Downtown Sarasota and the surrounding islands.</p>
  </article>
  <article class="tour tour--dark" style="left:259px;top:428px;width:222px">
    <h2 class="tour__head"><svg viewBox="0 0 26 22"><g fill="none" stroke="#0456a4" stroke-width="1.6"><path d="M3 3h20M13 3v4"/><circle cx="13" cy="12" r="5"/><path d="M7 20h12M10 17v3M16 17v3"/></g></svg>The ULTIMATE BEACH Tour</h2>
    <p class="tour__text">(Approx. 30-Minute flight time) Cruising along the world famous white sand beaches of Siesta Key after crossing the Bay front at Big Pass and over Bird Key along Longboat and Anna-Maria Island to see many of Sarasota’s spectacular beachfront homes and, possibly, some marine wildlife.</p>
  </article>
  <article class="tour tour--dark" style="left:259px;top:516px;width:222px">
    <h2 class="tour__head"><svg viewBox="0 0 26 22"><g fill="none" stroke="#0456a4" stroke-width="1.6"><path d="M3 3h20M13 3v4"/><circle cx="13" cy="12" r="5"/><path d="M7 20h12M10 17v3M16 17v3"/></g></svg>The SUNSET Tour</h2>
    <p class="tour__text">(Approx. 20-Minute flight time) Enjoy a breathtaking flight over Downtown Sarasota and the surrounding islands during sunset. This is one of our most romantic tour options and has served already a few times as a stage for marriage proposals and wedding anniversaries.</p>
  </article>

  <footer class="footer">
    <span class="footer__url">www.corvanefly.com</span>
    <span class="footer__phone"><svg viewBox="0 0 20 20"><circle cx="10" cy="10" r="9" fill="none" stroke="#fff" stroke-width="1.5"/><path d="M7 5.5 8.6 7.8 7.6 9a6 6 0 0 0 3.4 3.4l1.2-1 2.3 1.6-.9 1.6c-3.8.2-7.5-3.5-7.3-7.3Z" fill="#fff"/></svg>+1 (555) 014-2290</span>
  </footer>
</section>

</body>
</html>
```